Expense Tracker App for Young Adults

I need a mobile app designer to design an app UI for me. It is for an expense tracker app. I’ve attached a mind map of the various screens and features of the app.

I would like to see designs for this app which is targeted towards young adults (late teens & early 20s) just starting their career who want to plan their budgets and track their expenses.
Updates

Hello designers! I'm conscious that this is not a guaranteed project, so I can understand that some of you might be apprehensive. Just wanted to let you know that I'm willing to see your initial drafts that show your direction and theme for design. You don't have to design the whole app. In fact, it's better if you share your initial design ideas so that we can have a discussion and I can give my input. If I see some good initial designs, I will be happy to make this a guaranteed project. I'm simply being cautious since I'm bootstrapping this and funding out of my own pocket. Thank you for your understanding!

Target Market(s)

Young adults who are just starting their careers, late teens and early 20s.

Font styles to use
Sans Serif

Requirements
Must have
• Ease of use, smart and sleek, a guided setup wizard which will help users setup their account after signing up.
Should not have
• Clunky

```html
<!DOCTYPE html>
<html lang="en">
<head>
<meta charset="UTF-8">
<title>Expense Tracker – Dashboard</title>
<link href="https://fonts.googleapis.com/css2?family=Poppins:wght@300;400;500;600;700&display=swap" rel="stylesheet">
<style>
  :root {
    --bg: #ffffff;
    --ink: #2b2b3c;
    --muted: #8c8c99;
    --label: #7d7f95;
    --blue: #1f7ff0;
    --blue-soft: #d8e8fd;
    --yellow: #ffbb38;
    --pink: #ee22c0;
    --white: #ffffff;
    --card-shadow: rgba(40, 60, 120, 0.08);
  }
  * { margin: 0; padding: 0; box-sizing: border-box; }
  html, body {
    width: 1200px;
    height: 2598px;
    overflow: hidden;
    background: var(--bg);
    font-family: "Poppins", sans-serif;
  }
  .screen {
    position: absolute;
    left: 0; top: 0;
    width: 375px;
    height: 812px;
    transform: scale(3.2);
    transform-origin: 0 0;
    background: var(--bg);
  }
  .abs { position: absolute; }

  .greeting { left: 17px; top: 36px; color: var(--muted); font-size: 15px; font-weight: 400; line-height: 20px; }
  .user-name { left: 17px; top: 70px; color: var(--ink); font-size: 21.5px; font-weight: 600; line-height: 30px; letter-spacing: 0.1px; }
  .avatar {
    left: 310px; top: 48px; width: 48px; height: 48px; border-radius: 50%;
    background: radial-gradient(circle at 50% 60%, #3a3440 0%, #2a2530 35%, #8a5bd6 70%, #a06ae0 100%);
  }

  .balance-card {
    left: 17px; top: 139px; width: 341px; height: 177px;
    background: var(--blue); border-radius: 18px; color: var(--white);
  }
  .balance-title { left: 20px; top: 21px; font-size: 16.5px; font-weight: 400; opacity: 0.9; }
  .balance-amount { left: 20px; top: 61px; font-size: 20px; font-weight: 700; }
  .balance-item { top: 118px; font-size: 13.5px; font-weight: 500; line-height: 20px; }
  .balance-item span { display: block; margin-top: 5px; font-weight: 400; opacity: 0.9; }
  .go-btn {
    width: 30px; height: 30px; border-radius: 50%;
    display: flex; align-items: center; justify-content: center;
  }
  .go-btn.light { background: var(--white); }
  .go-btn.solid { background: var(--blue); }

  .expenses-card {
    left: 17px; top: 342px; width: 341px; height: 365px;
    background: var(--white); border-radius: 18px;
    box-shadow: 0 4px 22px var(--card-shadow);
  }
  .expenses-title { left: 20px; top: 21px; font-size: 17.5px; font-weight: 400; color: var(--ink); }
  .chart { left: 0; top: 0; }
  .chart-label { font-size: 12.5px; color: var(--label); line-height: 16px; }
  .expenses-total { left: 0; width: 341px; top: 334px; text-align: center; font-size: 11.5px; color: var(--label); }
  .expenses-total strong { color: var(--blue); font-weight: 500; }

  .tab-bar {
    left: 22px; top: 728px; width: 275px; height: 58px; border-radius: 29px;
    background: var(--white); box-shadow: 0 4px 20px var(--card-shadow);
  }
  .tab-active {
    left: 0; top: 0; width: 119px; height: 58px; border-radius: 29px;
    background: var(--blue); color: var(--white);
    display: flex; align-items: center; padding-left: 13px; gap: 9px;
    font-size: 12.5px; font-weight: 600;
  }
  .tab-icon { width: 18px; height: 18px; }
  .fab {
    left: 303px; top: 729px; width: 56px; height: 56px; border-radius: 50%;
    background: var(--blue); display: flex; align-items: center; justify-content: center;
    box-shadow: 0 6px 16px rgba(31, 127, 240, 0.3);
  }
</style>
</head>
<body>
<main class="screen">
  <header>
    <p class="abs greeting">Welcome,</p>
    <h1 class="abs user-name">Daniel Foster</h1>
    <div class="abs avatar" role="img" aria-label="Profile photo of the user"></div>
  </header>

  <section class="abs balance-card">
    <h2 class="abs balance-title">Your Current Balance</h2>
    <div class="abs go-btn light" style="left:295px; top:19px;">
      <svg width="12" height="12" viewBox="0 0 12 12"><path d="M4.5 2.5 8 6 4.5 9.5" fill="none" stroke="var(--blue)" stroke-width="2" stroke-linecap="round" stroke-linejoin="round"/></svg>
    </div>
    <p class="abs balance-amount">$4000</p>
    <p class="abs balance-item" style="left:20px;">Savings<span>$1000</span></p>
    <p class="abs balance-item" style="left:105px;">Cash<span>$500</span></p>
    <p class="abs balance-item" style="left:172px;">Accounts<span>$4000</span></p>
  </section>

  <section class="abs expenses-card">
    <h2 class="abs expenses-title">Expenses</h2>
    <div class="abs go-btn solid" style="left:295px; top:19px;">
      <svg width="12" height="12" viewBox="0 0 12 12"><path d="M4.5 2.5 8 6 4.5 9.5" fill="none" stroke="var(--white)" stroke-width="2" stroke-linecap="round" stroke-linejoin="round"/></svg>
    </div>

    <svg class="abs chart" width="341" height="365" viewBox="0 0 341 365">
      <g transform="translate(175 226) rotate(-90)">
        <circle r="77.5" fill="none" stroke="var(--blue)" stroke-width="17" stroke-dasharray="292.2 486.9"/>
        <circle r="77.5" fill="none" stroke="var(--yellow)" stroke-width="17" stroke-dasharray="146.1 486.9" stroke-dashoffset="-292.2"/>
        <circle r="77.5" fill="none" stroke="var(--pink)" stroke-width="17" stroke-dasharray="48.6 486.9" stroke-dashoffset="-438.3"/>
      </g>
      <!-- leader lines -->
      <line x1="152" y1="117" x2="152" y2="140" stroke="var(--pink)" stroke-width="1.2"/>
      <circle cx="152" cy="117" r="3.3" fill="var(--pink)"/>
      <line x1="71" y1="172" x2="109" y2="172" stroke="var(--yellow)" stroke-width="1.2"/>
      <circle cx="71" cy="172" r="3.3" fill="var(--yellow)"/>
      <line x1="226" y1="298" x2="241" y2="300" stroke="var(--blue)" stroke-width="1.2"/>
      <circle cx="241" cy="300" r="3.3" fill="var(--blue)"/>
      <!-- cart icon -->
      <g transform="translate(111 87)" fill="none" stroke="var(--pink)" stroke-width="1.5" stroke-linecap="round" stroke-linejoin="round">
        <path d="M1 1.5h2.2l2 9h8l1.8-6.5H4.2"/>
        <circle cx="6.3" cy="13.4" r="1"/>
        <circle cx="12.6" cy="13.4" r="1"/>
      </g>
      <!-- pizza icon -->
      <g transform="translate(7 164)" fill="none" stroke="var(--yellow)" stroke-width="1.5" stroke-linejoin="round">
        <path d="M2 15 7 1.5c4 1.4 7 4.5 8.3 8.5Z"/>
        <path d="M5.6 5.4c2.6.9 4.6 3 5.5 5.6"/>
        <circle cx="7" cy="10.3" r="0.9" fill="var(--yellow)" stroke="none"/>
      </g>
      <!-- car icon -->
      <g transform="translate(254 293)" fill="none" stroke="var(--blue)" stroke-width="1.5" stroke-linejoin="round">
        <path d="M1.5 9.5 3 4.5c.3-1 1-1.5 2-1.5h6c1 0 1.7.5 2 1.5l1.5 5v3h-13Z"/>
        <path d="M1.5 8.5h13"/>
        <circle cx="4.6" cy="10.6" r="0.8" fill="var(--blue)"/>
        <circle cx="11.4" cy="10.6" r="0.8" fill="var(--blue)"/>
      </g>
    </svg>
    <span class="abs chart-label" style="left:135px; top:87px;">Shopping</span>
    <span class="abs chart-label" style="left:28px; top:164px;">Food</span>
    <span class="abs chart-label" style="left:276px; top:292px;">Transport</span>

    <p class="abs expenses-total">Your Expenses for this month: <strong>$1000</strong></p>
  </section>

  <nav class="abs tab-bar">
    <div class="abs tab-active">
      <svg class="tab-icon" viewBox="0 0 18 18" fill="none" stroke="var(--white)" stroke-width="1.7">
        <rect x="1.5" y="1.5" width="5.5" height="5.5" rx="1.6"/>
        <rect x="11" y="1.5" width="5.5" height="5.5" rx="1.6"/>
        <rect x="1.5" y="11" width="5.5" height="5.5" rx="1.6"/>
        <rect x="11" y="11" width="5.5" height="5.5" rx="1.6"/>
      </svg>
      Dashboard
    </div>
    <svg class="abs tab-icon" style="left:136px; top:20px;" viewBox="0 0 18 18" fill="none" stroke="var(--ink)" stroke-width="1.7" stroke-linejoin="round">
      <rect x="1.5" y="3" width="15" height="12" rx="2"/>
      <path d="M1.5 7h15"/>
      <path d="M11.5 11h2"/>
    </svg>
    <svg class="abs tab-icon" style="left:186px; top:20px;" viewBox="0 0 18 18" fill="none" stroke="var(--ink)" stroke-width="1.7" stroke-linejoin="round">
      <circle cx="9" cy="9" r="7"/>
      <path d="M9 2v7l5 5"/>
    </svg>
    <svg class="abs tab-icon" style="left:235px; top:20px;" viewBox="0 0 18 18" fill="none" stroke="var(--ink)" stroke-width="1.7" stroke-linejoin="round">
      <path d="M9 1.5l1.4 1.9 2.3-.5.5 2.3 2.1 1.1-1 2.1 1 2.1-2.1 1.1-.5 2.3-2.3-.5L9 16.5l-1.4-1.9-2.3.5-.5-2.3-2.1-1.1 1-2.1-1-2.1 2.1-1.1.5-2.3 2.3.5Z"/>
      <circle cx="9" cy="9" r="2.4"/>
    </svg>
  </nav>

  <div class="abs fab">
    <svg width="18" height="18" viewBox="0 0 18 18" stroke="var(--white)" stroke-width="2" stroke-linecap="round">
      <path d="M9 2v14M2 9h14"/>
    </svg>
  </div>
</main>
</body>
</html>
```